Mediapreneur looking for Wordpress Design for 55 plus community

I own the domain brightyearsnook.com and I have another contest going on to design the logo. I'm looking to build a site for those 55 plus who are living an active lifestyle.
I want to base my site off of this site, except make it more friendly to the 55 and over community.
http://www.tallowcrest.com/
In my menu, I'd like to have the following categories. About Listen Read Watch Forum Contact and the ability to add more categories in the future (possible to external sites).
Listen will be podcasts, read will be blog posts, and watch will be videos (webinars)
Updates
I uploaded some images I bought from Pixelgrove that could be used in the design. Possibly a collage.
Videos are actually going to be webinars in the future. For example, I see a real estate agent presenting a webinar about active communities, or a financial adviser giving financial advice to my community. I was trying to simplify it for my audience, some of whom may not know what a webinar is, but I'd like to go with Webinar instead of Watch. I like read and listen, though. I plan on monetizing the site via sponsorship in podcasts and a directory of active communities I'm building. I'm possibly going to ask for sponsorship for webinars and write e-books in the future. Could you display podcasts on the home page? Maybe put the most recent blog posts below the podcasts? Also, can you put a form asking them to join my newsletter somewhere in prominent position? My call to actions are to get them to subscribe to my mailing list and listen to podcasts.
Thanks.
I changed my mind on using Webinar in the menu. I asked my mom what a webinar was and she gave me a blank look. I like the idea of using Watch instead. The menu should be in this order About Listen Read Watch Forum. Please put contact details in the header menu above the menu. Call...make up a phone number. Email..contact@brightyearsnook.com. In case you missed one of my previous public updates, Listen = Podcast, Read = Blog, and Watch = Webinar/Video.
Thanks and sorry for the changes.
55 and over
Build

```html
<!DOCTYPE html>
<html lang="en">
<head>
<meta charset="utf-8">
<title>Brightyearsnook – Active Lifestyle</title>
<link rel="stylesheet" href="https://fonts.googleapis.com/css2?family=Montserrat:wght@400;600;700&family=Open+Sans:wght@400;600&display=swap">
<style>
:root{
  --blue:#2f7fe0;
  --blue-light:#3d8ff0;
  --blue-dark:#2363c4;
  --logo-blue:#2b5fa9;
  --ink:#2b2b2b;
  --page:#f2f2f2;
  --white:#ffffff;
  --footer:#222222;
  --footer-bottom:#1a1a1a;
  --footer-text:#d6d6d6;
  --hero-top:#4f8dd3;
  --hero-bottom:#86aad2;
}
*{box-sizing:border-box;margin:0;padding:0}
html,body{width:1200px;height:2659px;overflow:hidden}
body{position:relative;background:var(--page);font-family:'Open Sans',Arial,sans-serif;color:var(--ink)}
svg{display:block}

/* Header */
.site-header{position:absolute;left:0;top:0;width:1200px;height:131px;background:var(--white);border-top:3px solid var(--blue-dark)}
.brand{position:absolute;left:133px;top:46px;font-family:'Montserrat',Arial,sans-serif;font-weight:700;font-size:27px;color:var(--logo-blue);letter-spacing:.3px}
.header-social{position:absolute;left:968px;top:32px;display:flex;gap:8px}
.header-social span{width:19px;height:19px;border-radius:50%}
.dot-a{background:#29a9e1}.dot-b{background:#3b5a9a}.dot-c{background:#d63b2b}.dot-d{background:#c4302b}
.main-nav{position:absolute;left:555px;top:82px;font-family:'Montserrat',Arial,sans-serif;font-size:11.5px;font-weight:600;color:#333}
.main-nav a{position:absolute;white-space:nowrap;text-decoration:none;color:inherit}
.main-nav .active{color:var(--blue)}
.nav-underline{position:absolute;left:552px;top:126px;width:44px;height:3px;background:var(--blue)}

/* Hero */
.hero{position:absolute;left:0;top:131px;width:1200px;height:500px;overflow:hidden}
.hero-photo{position:absolute;inset:0;background:linear-gradient(180deg,var(--hero-top),var(--hero-bottom))}
.hero-title{position:absolute;left:133px;top:105px;font-family:'Montserrat',Arial,sans-serif;font-weight:700;font-size:37px;color:var(--white);letter-spacing:.5px}
.hero-text{position:absolute;left:133px;top:170px;width:380px;font-size:12px;line-height:21px;color:var(--white)}
.hero-btn{position:absolute;left:135px;top:232px;width:135px;height:39px;border-radius:20px;background:#e4e4e4;font-family:'Montserrat',Arial,sans-serif;font-size:11px;font-weight:600;color:#333;display:flex;align-items:center;justify-content:center}
.hero-dots{position:absolute;left:133px;top:302px;display:flex;gap:8px}
.hero-dots span{width:7px;height:7px;border-radius:50%;background:var(--white)}
.hero-dots .on{background:var(--blue)}

/* Feature band */
.feature-band{position:absolute;left:0;top:631px;width:1200px;height:277px;background:linear-gradient(180deg,var(--blue-light),var(--blue-dark));display:flex;justify-content:center}
.features{display:flex;width:1060px}
.feature{width:353px;text-align:center;color:var(--white);position:relative}
.feature + .feature::before{content:"";position:absolute;left:0;top:80px;height:150px;border-left:1px solid rgba(255,255,255,.25)}
.feature-icon{width:102px;height:102px;border-radius:50%;background:var(--white);margin:36px auto 0;display:flex;align-items:center;justify-content:center}
.feature h2{font-family:'Montserrat',Arial,sans-serif;font-size:20px;font-weight:700;margin-top:20px;letter-spacing:.5px}
.feature p{font-size:11px;line-height:19.5px;width:260px;margin:12px auto 0}

/* Posts */
.posts{position:absolute;left:129px;top:966px;width:584px;display:flex;flex-direction:column;gap:32px}
.post-card{background:var(--white);box-shadow:0 2px 5px rgba(0,0,0,.15);height:312px}
.card-head{height:89px;background:linear-gradient(180deg,var(--blue-light),var(--blue-dark));display:flex;align-items:center;padding:0 28px 0 29px}
.card-head h3{font-family:'Montserrat',Arial,sans-serif;font-size:19px;font-weight:700;color:var(--white);flex:1;white-space:nowrap}
.card-tools{display:flex;gap:19px}
.post-body{display:flex;padding:21px 31px 0 22px}
.post-photo{width:193px;height:177px;flex:none}
.photo-1{background:linear-gradient(135deg,#8fae4e,#d9b59a)}
.photo-2{background:linear-gradient(135deg,#c9d6e6,#3f6fb4)}
.photo-3{background:linear-gradient(135deg,#e6e0da,#b9c4d4)}
.photo-4{background:linear-gradient(135deg,#5a4638,#c9a58e)}
.post-text{margin-left:19px;font-size:11.2px;line-height:19.5px;text-align:justify;color:#333}
.post-text p + p{margin-top:11px}
.keep-reading{display:block;margin-top:2px;font-family:'Montserrat',Arial,sans-serif;font-size:10px;color:var(--blue-dark);letter-spacing:.5px}
.next-page{position:absolute;left:600px;top:2325px;width:113px;text-align:right;font-family:'Montserrat',Arial,sans-serif;font-size:10px;color:var(--blue-dark);text-decoration:underline}

/* Sidebar */
.sidebar-box{position:absolute;left:736px;width:328px;background:var(--white);box-shadow:0 2px 5px rgba(0,0,0,.15)}
.box-head{height:64px;background:linear-gradient(180deg,var(--blue-light),var(--blue-dark));display:flex;align-items:center;padding-left:22px;font-family:'Montserrat',Arial,sans-serif;font-size:19px;font-weight:700;color:var(--white)}
.search-box{top:966px;height:177px}
.search-field{position:absolute;left:23px;top:87px;width:281px;height:58px;border:1px solid #ddd;background:linear-gradient(180deg,#f3f3f3,#fff);display:flex;align-items:center;padding-left:16px}
.promo{position:absolute;left:734px;width:328px;overflow:hidden;color:var(--white)}
.promo-active{top:1175px;height:238px;background:linear-gradient(110deg,#1f2a1c,#6a705e)}
.promo-kicker{position:absolute;left:23px;top:46px;font-family:'Montserrat',Arial,sans-serif;font-size:19px;letter-spacing:.5px}
.promo-big{position:absolute;left:16px;top:76px;font-family:'Montserrat',Arial,sans-serif;font-weight:700;font-size:38px}
.promo-btn{position:absolute;left:18px;top:138px;width:99px;height:36px;background:var(--blue);border-radius:2px;font-family:'Montserrat',Arial,sans-serif;font-size:10.5px;font-weight:600;display:flex;align-items:center;justify-content:center}
.featured-box{top:1441px;height:574px}
.featured-list{list-style:none;padding:25px 22px 0 19px}
.featured-item{display:flex;height:92px;margin-bottom:27px}
.thumb{width:101px;height:92px;flex:none;border-radius:3px}
.thumb-1{background:linear-gradient(135deg,#5b7fb0,#cfb9a6)}
.thumb-2{background:linear-gradient(135deg,#8fae6e,#dfc8b6)}
.thumb-3{background:linear-gradient(135deg,#bcc6d2,#d9b9a0)}
.thumb-4{background:linear-gradient(135deg,#79a0cf,#e2cbb6)}
.featured-copy{margin-left:14px}
.featured-copy h4{font-family:'Montserrat',Arial,sans-serif;font-size:14px;font-weight:700;line-height:23px;color:var(--blue-dark);margin-top:6px}
.featured-copy p{font-size:10.5px;line-height:19px;color:#444;text-align:justify;margin-top:5px}
.promo-listen{left:737px;top:2047px;height:252px;background:linear-gradient(135deg,#2b2826,#4e443e);text-align:center}
.promo-listen .kicker{margin-top:62px;font-family:'Montserrat',Arial,sans-serif;font-size:19px}
.promo-listen .big{margin-top:4px;font-family:'Montserrat',Arial,sans-serif;font-weight:700;font-size:37px}
.promo-listen svg{margin:4px auto 0}

/* Footer */
.site-footer{position:absolute;left:0;top:2366px;width:1200px;height:232px;background:var(--footer);color:var(--footer-text)}
.footer-brand{position:absolute;left:133px;top:40px;font-family:'Montserrat',Arial,sans-serif;font-weight:700;font-size:20px;color:#8a8a8a;white-space:nowrap}
.footer-social{position:absolute;left:136px;top:84px;display:flex;gap:10px}
.footer-social span{width:22px;height:22px;border-radius:50%;background:#111}
.footer-col{position:absolute;top:30px}
.footer-col h5{font-family:'Montserrat',Arial,sans-serif;font-size:13.5px;font-weight:400;letter-spacing:1px;color:#eee}
.quick-links{left:385px}
.quick-links ul{list-style:none;margin-top:20px;font-size:10.5px;line-height:19.5px}
.newsletter{left:592px}
.newsletter p{margin-top:20px;font-size:10.5px;line-height:19.5px;width:210px}
.news-input{margin-top:10px;width:208px;height:36px;background:#333;font-size:10.5px;color:#ccc;padding-left:12px;display:flex;align-items:center;letter-spacing:.5px}
.news-btn{margin-top:14px;width:83px;height:30px;background:var(--blue);border-radius:2px;font-size:10.5px;color:var(--white);display:flex;align-items:center;justify-content:center}
.contact{left:876px}
.contact ul{list-style:none;margin-top:24px;font-size:10.5px}
.contact li{display:flex;align-items:flex-start;gap:10px;margin-bottom:12px;line-height:15px}
.contact li svg{flex:none;margin-top:1px}
.contact a{color:inherit;text-decoration:underline}
.footer-bottom{position:absolute;left:0;top:2598px;width:1200px;height:61px;background:var(--footer-bottom);color:#ddd;font-size:10.5px;display:flex;align-items:center;justify-content:center}
</style>
</head>
<body>

<header class="site-header">
  <div class="brand">BRIGHTYEARSNOOK</div>
  <div class="header-social" aria-label="Social links">
    <span class="dot-a"></span><span class="dot-b"></span><span class="dot-c"></span><span class="dot-d"></span>
  </div>
  <nav class="main-nav">
    <a class="active" style="left:0">HOME</a>
    <a style="left:76px">ABOUT</a>
    <a style="left:150px">LISTEN</a>
    <a style="left:225px">READ</a>
    <a style="left:294px">WATCH</a>
    <a style="left:372px">FORUM</a>
    <a style="left:455px">CONTACT</a>
  </nav>
  <div class="nav-underline"></div>
</header>

<section class="hero">
  <div class="hero-photo" role="img" aria-label="Older man doing push-ups on grass under a blue sky"></div>
  <h1 class="hero-title">ACTIVE LIFESTYLE</h1>
  <p class="hero-text">Nemo enim ipsam voluptatem quia voluptas sit aspernatur aut odit aut fugit, sed quia consequuntur</p>
  <div class="hero-btn">LEARN MORE</div>
  <div class="hero-dots"><span class="on"></span><span></span><span></span></div>
</section>

<section class="feature-band">
  <div class="features">
    <div class="feature">
      <div class="feature-icon">
        <svg width="38" height="38" viewBox="0 0 38 38" fill="none" stroke="#2f6fd0" stroke-width="1.6"><path d="M4 8h18M4 15h18M4 22h12"/><path d="M28 6v22"/><path d="M28 6l6 3"/><circle cx="24.5" cy="28" r="3.5"/></svg>
      </div>
      <h2>LISTEN</h2>
      <p>Nemo enim ipsam voluptatem quia voluptas sit aspernatur aut odit aut</p>
    </div>
    <div class="feature">
      <div class="feature-icon">
        <svg width="38" height="38" viewBox="0 0 38 38" fill="none" stroke="#2f6fd0" stroke-width="1.6"><rect x="8" y="5" width="22" height="27" rx="1"/><path d="M8 26h22M14 5v14l3-2 3 2V5"/></svg>
      </div>
      <h2>READ</h2>
      <p>Nemo enim ipsam voluptatem quia voluptas sit aspernatur aut odit aut</p>
    </div>
    <div class="feature">
      <div class="feature-icon">
        <svg width="38" height="38" viewBox="0 0 38 38" fill="none" stroke="#2f6fd0" stroke-width="1.6"><rect x="4" y="7" width="30" height="20" rx="1"/><path d="M19 27v5M13 32h12"/></svg>
      </div>
      <h2>WATCH</h2>
      <p>Nemo enim ipsam voluptatem quia voluptas sit aspernatur aut odit aut</p>
    </div>
  </div>
</section>

<main class="posts">
  <article class="post-card">
    <div class="card-head">
      <h3>LOREM IPSUM DOLOR SIT AMET</h3>
      <div class="card-tools">
        <svg width="34" height="34" viewBox="0 0 34 34" fill="none" stroke="#fff" stroke-width="1.8"><circle cx="17" cy="18" r="13"/><path d="M17 10v8l5 4"/><path d="M8 6l-3 3"/></svg>
        <svg width="34" height="34" viewBox="0 0 34 34" fill="none" stroke="#fff" stroke-width="1.8"><circle cx="8" cy="17" r="4"/><circle cx="26" cy="7" r="4"/><circle cx="26" cy="27" r="4"/><path d="M11.5 15l11-6M11.5 19l11 6"/></svg>
        <svg width="34" height="34" viewBox="0 0 34 34" fill="none" stroke="#fff" stroke-width="1.8"><path d="M11 8H5v22h24V8h-6"/><path d="M17 3v17M11 14l6 6 6-6"/></svg>
        <svg width="34" height="34" viewBox="0 0 34 34" fill="none" stroke="#fff" stroke-width="1.8"><path d="M9 5l20 12-20 12z"/></svg>
      </div>
    </div>
    <div class="post-body">
      <div class="post-photo photo-1" role="img" aria-label="Smiling older couple outdoors"></div>
      <div class="post-text">
        <p>Lorem ipsum dolor sit amet, consectetur adipiscing elit, sed do eiusmod tempor incididunt ut labore et dolore magna aliqua. Ut enim ad minim veniam, quis nostrud exercitation ullamco laboris nisi ut aliquip ex ea commodo consequat.</p>
        <p>Nemo enim ipsam voluptatem quia voluptas sit aspernatur aut odit aut fugit, sed quia consequuntur magni dolores eos qui ratione voluptatem sequi nesciunt.</p>
        <span class="keep-reading">KEEP READING »</span>
      </div>
    </div>
  </article>

  <article class="post-card">
    <div class="card-head">
      <h3>LOREM IPSUM DOLOR SIT AMET</h3>
      <div class="card-tools">
        <svg width="34" height="34" viewBox="0 0 34 34" fill="none" stroke="#fff" stroke-width="1.8"><circle cx="17" cy="18" r="13"/><path d="M17 10v8l5 4"/><path d="M8 6l-3 3"/></svg>
        <svg width="34" height="34" viewBox="0 0 34 34" fill="none" stroke="#fff" stroke-width="1.8"><circle cx="8" cy="17" r="4"/><circle cx="26" cy="7" r="4"/><circle cx="26" cy="27" r="4"/><path d="M11.5 15l11-6M11.5 19l11 6"/></svg>
        <svg width="34" height="34" viewBox="0 0 34 34" fill="none" stroke="#fff" stroke-width="1.8"><path d="M11 8H5v22h24V8h-6"/><path d="M17 3v17M11 14l6 6 6-6"/></svg>
        <svg width="34" height="34" viewBox="0 0 34 34" fill="none" stroke="#fff" stroke-width="1.8"><path d="M9 5l20 12-20 12z"/></svg>
      </div>
    </div>
    <div class="post-body">
      <div class="post-photo photo-2" role="img" aria-label="Older couple smiling close together"></div>
      <div class="post-text">
        <p>Lorem ipsum dolor sit amet, consectetur adipiscing elit, sed do eiusmod tempor incididunt ut labore et dolore magna aliqua. Ut enim ad minim veniam, quis nostrud exercitation ullamco laboris nisi ut aliquip ex ea commodo consequat.</p>
        <p>Nemo enim ipsam voluptatem quia voluptas sit aspernatur aut odit aut fugit, sed quia consequuntur magni dolores eos qui ratione voluptatem sequi nesciunt.</p>
        <span class="keep-reading">KEEP READING »</span>
      </div>
    </div>
  </article>

  <article class="post-card">
    <div class="card-head">
      <h3>LOREM IPSUM DOLOR SIT AMET</h3>
      <div class="card-tools">
        <svg width="34" height="34" viewBox="0 0 34 34" fill="none" stroke="#fff" stroke-width="1.8"><circle cx="17" cy="18" r="13"/><path d="M17 10v8l5 4"/><path d="M8 6l-3 3"/></svg>
        <svg width="34" height="34" viewBox="0 0 34 34" fill="none" stroke="#fff" stroke-width="1.8"><circle cx="8" cy="17" r="4"/><circle cx="26" cy="7" r="4"/><circle cx="26" cy="27" r="4"/><path d="M11.5 15l11-6M11.5 19l11 6"/></svg>
        <svg width="34" height="34" viewBox="0 0 34 34" fill="none" stroke="#fff" stroke-width="1.8"><path d="M11 8H5v22h24V8h-6"/><path d="M17 3v17M11 14l6 6 6-6"/></svg>
        <svg width="34" height="34" viewBox="0 0 34 34" fill="none" stroke="#fff" stroke-width="1.8"><path d="M9 5l20 12-20 12z"/></svg>
      </div>
    </div>
    <div class="post-body">
      <div class="post-photo photo-3" role="img" aria-label="Smiling older woman holding glasses"></div>
      <div class="post-text">
        <p>Lorem ipsum dolor sit amet, consectetur adipiscing elit, sed do eiusmod tempor incididunt ut labore et dolore magna aliqua. Ut enim ad minim veniam, quis nostrud exercitation ullamco laboris nisi ut aliquip ex ea commodo consequat.</p>
        <p>Nemo enim ipsam voluptatem quia voluptas sit aspernatur aut odit aut fugit, sed quia consequuntur magni dolores eos qui ratione voluptatem sequi nesciunt.</p>
        <span class="keep-reading">KEEP READING »</span>
      </div>
    </div>
  </article>

  <article class="post-card">
    <div class="card-head">
      <h3>LOREM IPSUM DOLOR SIT AMET</h3>
      <div class="card-tools">
        <svg width="34" height="34" viewBox="0 0 34 34" fill="none" stroke="#fff" stroke-width="1.8"><circle cx="17" cy="18" r="13"/><path d="M17 10v8l5 4"/><path d="M8 6l-3 3"/></svg>
        <svg width="34" height="34" viewBox="0 0 34 34" fill="none" stroke="#fff" stroke-width="1.8"><circle cx="8" cy="17" r="4"/><circle cx="26" cy="7" r="4"/><circle cx="26" cy="27" r="4"/><path d="M11.5 15l11-6M11.5 19l11 6"/></svg>
        <svg width="34" height="34" viewBox="0 0 34 34" fill="none" stroke="#fff" stroke-width="1.8"><path d="M11 8H5v22h24V8h-6"/><path d="M17 3v17M11 14l6 6 6-6"/></svg>
        <svg width="34" height="34" viewBox="0 0 34 34" fill="none" stroke="#fff" stroke-width="1.8"><path d="M9 5l20 12-20 12z"/></svg>
      </div>
    </div>
    <div class="post-body">
      <div class="post-photo photo-4" role="img" aria-label="Elderly woman smiling with hands clasped"></div>
      <div class="post-text">
        <p>Lorem ipsum dolor sit amet, consectetur adipiscing elit, sed do eiusmod tempor incididunt ut labore et dolore magna aliqua. Ut enim ad minim veniam, quis nostrud exercitation ullamco laboris nisi ut aliquip ex ea commodo consequat.</p>
        <p>Nemo enim ipsam voluptatem quia voluptas sit aspernatur aut odit aut fugit, sed quia consequuntur magni dolores eos qui ratione voluptatem sequi nesciunt.</p>
        <span class="keep-reading">KEEP READING »</span>
      </div>
    </div>
  </article>
</main>
<a class="next-page">NEXT PAGE »</a>

<aside>
  <section class="sidebar-box search-box">
    <div class="box-head">SEARCH</div>
    <div class="search-field">
      <svg width="14" height="14" viewBox="0 0 14 14" fill="none" stroke="#888" stroke-width="1.3"><circle cx="6" cy="6" r="4.5"/><path d="M9.5 9.5l3.5 3.5"/></svg>
    </div>
  </section>

  <section class="promo promo-active">
    <div style="position:absolute;inset:0" role="img" aria-label="Older woman relaxing with a cup of tea"></div>
    <div class="promo-kicker">WHO ARE LIVING</div>
    <div class="promo-big">ACTIVE</div>
    <div class="promo-btn">VIEW DETAILS</div>
  </section>

  <section class="sidebar-box featured-box">
    <div class="box-head">FEATURED POSTS</div>
    <ul class="featured-list">
      <li class="featured-item"><div class="thumb thumb-1" role="img" aria-label="Older couple together"></div><div class="featured-copy"><h4>LOREM IPSUM<br>DOLOR</h4><p>Neque porro quisquam est, qui dolorem ipsum quia</p></div></li>
      <li class="featured-item"><div class="thumb thumb-2" role="img" aria-label="Older couple outdoors"></div><div class="featured-copy"><h4>LOREM IPSUM<br>DOLOR</h4><p>Neque porro quisquam est, qui dolorem ipsum quia</p></div></li>
      <li class="featured-item"><div class="thumb thumb-3" role="img" aria-label="Smiling older man"></div><div class="featured-copy"><h4>LOREM IPSUM<br>DOLOR</h4><p>Neque porro quisquam est, qui dolorem ipsum quia</p></div></li>
      <li class="featured-item"><div class="thumb thumb-4" role="img" aria-label="Older couple hugging"></div><div class="featured-copy"><h4>LOREM IPSUM<br>DOLOR</h4><p>Neque porro quisquam est, qui dolorem ipsum quia</p></div></li>
    </ul>
  </section>

  <section class="promo promo-listen" role="img" aria-label="Older man listening with headphones">
    <div class="kicker">ACTIVE LIFESTYLE</div>
    <div class="big">LISTEN</div>
    <svg width="46" height="40" viewBox="0 0 46 40" fill="none" stroke="#fff" stroke-width="3.5"><path d="M6 30V22a17 17 0 0 1 34 0v8"/><rect x="5" y="25" width="8" height="12" rx="2" fill="#fff"/><rect x="33" y="25" width="8" height="12" rx="2" fill="#fff"/></svg>
  </section>
</aside>

<footer class="site-footer">
  <div class="footer-brand">BRIGHTYEARSNOOK</div>
  <div class="footer-social"><span></span><span></span><span></span><span></span><span></span></div>
  <div class="footer-col quick-links">
    <h5>Quick Links</h5>
    <ul><li>Home</li><li>About</li><li>Listen</li><li>Read</li><li>Watch</li><li>Forum</li><li>Contact</li></ul>
  </div>
  <div class="footer-col newsletter">
    <h5>Newsletter</h5>
    <p>Subscribe newsletter to receive the latest news Updates</p>
    <div class="news-input">Enter Your Mail Id</div>
    <div class="news-btn">Subscribe</div>
  </div>
  <div class="footer-col contact">
    <h5>Contact us</h5>
    <ul>
      <li><svg width="14" height="13" viewBox="0 0 14 13" fill="#fff"><path d="M1 4c0-2 2-3 6-3s6 1 6 3v1h-3V3.5H4V5H1z"/><rect x="2" y="6" width="10" height="6" rx="1"/></svg>248-555-0171</li>
      <li><svg width="14" height="13" viewBox="0 0 14 13" fill="#fff"><rect x="3" y="0" width="8" height="4"/><rect x="0" y="4" width="14" height="6" rx="1"/><rect x="3" y="8" width="8" height="5" fill="#222" stroke="#fff"/></svg>248-555-0184</li>
      <li><svg width="14" height="11" viewBox="0 0 14 11" fill="none" stroke="#fff" stroke-width="1.4"><rect x="1" y="1" width="12" height="9"/><path d="M1 1l6 5 6-5"/></svg><a>hello@brightyearsnook.com</a></li>
      <li><svg width="14" height="14" viewBox="0 0 14 14" fill="#fff"><path d="M7 0a5 5 0 0 1 5 5c0 4-5 9-5 9S2 9 2 5a5 5 0 0 1 5-5z"/><circle cx="7" cy="5" r="2" fill="#222"/></svg><span>#2865 Lorem ipsum dolor sit amet,<br>consectetur adipiscing elit</span></li>
    </ul>
  </div>
</footer>
<div class="footer-bottom">2016© brightyearsnook.com. All Right Reserved</div>

</body>
</html>
```